Business Cards - New Logo Rebranding

Hello We know have a red and blue logo and are looking to create new cards. We are looking for the best creativity of the new logo merged with some of the existing artwork provided.

Target Market(s)

Realtors

Industry/Entity Type

Real Estate

Contact Information for Business Card

New logo with rebranded colors

Requirements
Must have
• Creative use of the new logo

```html
<!DOCTYPE html>
<html lang="en">
<head>
<meta charset="utf-8">
<title>Summit Crest – Business Card</title>
<link href="https://fonts.googleapis.com/css2?family=Open+Sans:wght@400;600;700&display=swap" rel="stylesheet">
<style>
  :root {
    --backdrop: #969696;
    --card-white: #ffffff;
    --brand-blue: #0e73bb;
    --brand-red: #df373d;
    --text-grey: #6f6f6f;
    --divider: #8fa3d6;
  }
  html, body {
    margin: 0;
    padding: 0;
    width: 1200px;
    height: 1000px;
    overflow: hidden;
    background: var(--backdrop);
    font-family: "Open Sans", Arial, sans-serif;
  }
  .card {
    position: absolute;
    left: 211px;
    width: 778px;
    height: 448px;
    display: block;
  }
  .card--front { top: 21px; }
  .card--back { top: 500px; }
  .brand-name { font-weight: 700; fill: var(--brand-blue); }
  .person-first { font-weight: 600; fill: var(--brand-blue); }
  .person-last { font-weight: 600; fill: var(--brand-red); }
  .person-title { font-weight: 400; fill: var(--text-grey); }
  .contact-line { font-weight: 400; fill: var(--text-grey); }
  .web-address { font-weight: 700; fill: var(--card-white); }
  .back-brand { font-weight: 700; fill: var(--card-white); }
</style>
</head>
<body>

<svg class="card card--front" viewBox="0 0 778 448" xmlns="http://www.w3.org/2000/svg">
  <defs>
    <clipPath id="front-shape"><rect width="778" height="448" rx="27"/></clipPath>
  </defs>
  <g clip-path="url(#front-shape)">
    <rect width="778" height="448" fill="var(--card-white)"/>
    <path class="footer-band" d="M0 341 C160 385 300 390 320 388 L390 388 C560 386 700 345 778 322 L778 448 L0 448 Z" fill="var(--brand-red)"/>
  </g>

  <g class="brand-lockup">
    <circle cx="90" cy="226" r="20" fill="var(--brand-red)"/>
    <text class="brand-name" x="120" y="237" font-size="30">SUMMIT CREST</text>
  </g>

  <line class="divider" x1="390" y1="87" x2="390" y2="302" stroke="var(--divider)" stroke-width="1"/>

  <g class="contact-block" text-anchor="middle">
    <text x="561" y="156" font-size="28" letter-spacing="-0.8">
      <tspan class="person-first">Dana</tspan> <tspan class="person-last">Whitfield</tspan>
    </text>
    <text class="person-title" x="561" y="180" font-size="17">Title</text>

    <g class="contact-icons">
      <circle cx="529" cy="202" r="12" fill="var(--brand-red)"/>
      <path d="M524 196 q-2 2 0 6 q3 5 8 7 q3 1 4 -1 l-3 -3 l-2 1 q-3 -2 -4 -5 l1 -2 z" fill="var(--card-white)"/>
      <circle cx="560" cy="202" r="12" fill="var(--brand-red)"/>
      <rect x="556" y="194" width="8" height="15" rx="1.5" fill="var(--card-white)"/>
      <rect x="557.5" y="196" width="5" height="9" fill="var(--brand-red)"/>
      <circle cx="591" cy="202" r="12" fill="var(--brand-red)"/>
      <rect x="584" y="197" width="14" height="10" fill="none" stroke="var(--card-white)" stroke-width="1.6"/>
      <path d="M584 197 L591 203 L598 197 M584 207 L589 202 M598 207 L593 202" fill="none" stroke="var(--card-white)" stroke-width="1.3"/>
    </g>

    <text class="contact-line" x="561" y="235" font-size="17">800.555.0142</text>
    <text class="contact-line" x="561" y="256" font-size="17">562.555.0193</text>
    <text class="contact-line" x="561" y="277" font-size="17">dana@summitcrestinspect.com</text>
  </g>

  <text class="web-address" x="389" y="427" font-size="28" text-anchor="middle">www.summitcrestinspect.com</text>
</svg>

<svg class="card card--back" viewBox="0 0 778 448" xmlns="http://www.w3.org/2000/svg">
  <defs>
    <clipPath id="back-shape"><rect width="778" height="448" rx="27"/></clipPath>
  </defs>
  <g clip-path="url(#back-shape)">
    <rect width="778" height="448" fill="var(--brand-blue)"/>
    <path class="white-sweep" d="M0 351 C150 410 300 417 340 416 C520 412 680 365 778 322 L778 448 L0 448 Z" fill="var(--card-white)"/>
    <path class="red-sweep" d="M0 383 C120 445 240 460 330 462 L778 462 L778 345 C690 380 580 420 480 448 L778 448 Z" fill="var(--brand-red)"/>
    <path class="red-sweep" d="M0 383 C100 435 200 448 230 448 L0 448 Z" fill="var(--brand-red)"/>
    <path class="red-sweep" d="M480 448 C600 425 700 385 778 345 L778 448 Z" fill="var(--brand-red)"/>
  </g>

  <g class="back-brand-lockup">
    <circle cx="170" cy="190" r="26" fill="var(--card-white)"/>
    <text class="back-brand" x="212" y="205" font-size="44">SUMMIT CREST</text>
  </g>
</svg>

</body>
</html>
```